Masterfolien & mehr | Branche Gesundheit | Anschlussaufträge
Tolle Leistung, netter Kontakt, verdienter Gewinner!
Zielgruppe
Sonnquell ist Dienstleister im Bereich 'Betriebliches Gesundheitsmanagement'. Zielgruppe sind Unternehmen zahlreicher Branchen, die die Gesundheit ihrer Mitarbeiter untersuchen und verbessern wollen.
Aufgabenstellung
Bitte möglichst Startfolie, Folie mit Aufzählungen und Text und Folie mit Bild und Text und Kontaktfolie.
Beispieltexte und eine entsprechende Folienansicht habe ich beigefügt, das könnte helfen.
Die Präsentation soll als E-Mail-Anhang im Nachgang eines Akquiseanrufs genutzt werden und über Produkte und Lösungen informieren.
Bitte Farbgebung berücksichtigen. Blau: 90/51/0/0, grau dunkel: 68/51/58/30, grau hell: 40/33/49/1
Schriften: Offen für Vorschläge, möglichst freie Schriften oder klassische Linotype.
Wir würden den Gewinner gern mit weiteren Aufträgen versehen, z.B. die Vorlage mit vorgegebenen Inhalten füllen, Flussdiagramme erstellen, Schaubilder erstellen etc..

```html
<!DOCTYPE html>
<html lang="de">
<head>
<meta charset="utf-8">
<title>Investition in Gesundheit – Warum?</title>
<link href="https://fonts.googleapis.com/css2?family=Oswald:wght@500;700&family=Arimo:wght@400;700&display=swap" rel="stylesheet">
<style>
  :root {
    --blue: #0b6db7;
    --grey-dark: #4c5651;
    --grey-light: #a79f87;
    --ink: #1f1f1f;
    --white: #ffffff;
  }
  * { box-sizing: border-box; margin: 0; padding: 0; }
  html, body { width: 1200px; height: 848px; overflow: hidden; background: var(--white); }
  .slide { position: relative; width: 1200px; height: 848px; background: var(--white); font-family: "Arimo", Arial, sans-serif; }

  .title-band { position: absolute; left: 0; top: 53px; width: 982px; height: 84px; background: var(--blue); }
  .title-band .marker { position: absolute; left: 0; top: 32px; }
  .title-band h1 {
    position: absolute; left: 51px; top: 12px;
    font-family: "Oswald", sans-serif; font-weight: 700; font-style: italic;
    font-size: 42px; line-height: 56px; color: var(--white); letter-spacing: 0.2px;
  }

  .brand { position: absolute; left: 1008px; top: 70px; display: flex; align-items: center; gap: 8px; }
  .brand .dot { width: 14px; height: 14px; border-radius: 50%; background: var(--grey-dark); }
  .brand span { font-family: "Oswald", sans-serif; font-weight: 700; font-style: italic; font-size: 28px; color: var(--grey-dark); }

  .panel { position: absolute; border: 2px solid var(--grey-light); border-top: none; background: var(--white); }
  .panel h2 {
    height: 58px; background: var(--blue); color: var(--white);
    font-size: 21px; font-weight: 700; line-height: 58px; padding-left: 17px; margin: 0 -2px;
  }
  .panel-company { left: 53px; top: 207px; width: 354px; height: 499px; }
  .panel-person { left: 425px; top: 207px; width: 557px; height: 260px; }

  .point { position: absolute; font-size: 15.5px; line-height: 20px; color: var(--ink); }
  .point.marked::before {
    content: ""; position: absolute; left: -17px; top: 3px;
    border-left: 11px solid var(--blue); border-top: 7px solid transparent; border-bottom: 7px solid transparent;
  }
  .panel-company .point { left: 15px; }
  .panel-person .point { left: 15px; }

  .arrows { position: absolute; left: 0; top: 0; }

  .result {
    position: absolute; left: 593px; top: 557px; width: 387px; height: 71px;
    border: 3px solid var(--blue); display: flex; align-items: center; justify-content: center;
    font-family: "Oswald", sans-serif; font-weight: 700; font-style: italic; font-size: 42px; color: var(--blue);
  }

  .footer { position: absolute; top: 776px; font-family: "Oswald", sans-serif; font-weight: 700; font-style: italic; font-size: 16px; color: var(--grey-dark); }
  .footer-left { left: 51px; }
  .footer-right { right: 69px; }
</style>
</head>
<body>
<div class="slide">
  <header class="title-band">
    <svg class="marker" width="12" height="22" viewBox="0 0 12 22"><polygon points="0,0 11,11 0,22" fill="#ffffff"/></svg>
    <h1>Investition in Gesundheit - Warum?</h1>
  </header>

  <div class="brand"><div class="dot"></div><span>Sonnquell</span></div>

  <section class="panel panel-company">
    <h2>UNTERNEHMEN</h2>
    <p class="point marked" style="top:90px">Langfristig weniger Krankheitstage -<br>Kostensenkung</p>
    <p class="point marked" style="top:152px">Reduzierte Personalfluktuation -<br>Mitarbeiterbindung</p>
    <p class="point marked" style="top:214px">Produktivität</p>
    <p class="point" style="top:254px">Wettbewerbsfähigkeit</p>
    <p class="point" style="top:295px">Unternehmensimage</p>
    <p class="point" style="top:335px">Leistungsfähigkeit</p>
    <p class="point" style="top:377px">Arbeitszufriedenheit/<br>Betriebsklima</p>
    <p class="point" style="top:438px">Motivation</p>
  </section>

  <section class="panel panel-person">
    <h2>INDIVIDUUM</h2>
    <p class="point marked" style="top:90px">Steigerung des Gesundheitsbewusstseins</p>
    <p class="point marked" style="top:131px">Ausgleich &amp; Entspannung</p>
    <p class="point marked" style="top:173px">Freude &amp; Spaß</p>
    <p class="point marked" style="top:214px">Lebensqualität</p>
  </section>

  <svg class="arrows" width="1200" height="848" viewBox="0 0 1200 848">
    <polygon points="305,418 355,466 319,466 319,653 292,653 292,466 256,466" fill="var(--blue)"/>
    <polygon points="777,415 795,415 795,485 824,485 786,523 751,485 777,485" fill="var(--grey-dark)"/>
    <polygon points="390,584 513,584 513,559 552,595 513,631 513,602 390,602" fill="var(--grey-dark)"/>
  </svg>

  <div class="result">WIN - WIN SITUATION</div>

  <footer>
    <p class="footer footer-left">SONNQUELL UG | 2018</p>
    <p class="footer footer-right">01</p>
  </footer>
</div>
</body>
</html>
```